Business card for hi tech component manufacturer, specialising in after market firearms components a
Tovin Industries (Ti)
Use same font as used in my logo
Owen Petrie
General Manager
Postal: PO Box 58491, Brackley, Christchurch 8245, New Zealand
Physical: 14 Garnet Street, Fenwick, Christchurch 8024, New Zealand
sales@tovin-works.example.nz
tovin-works.example.nz
Details are to be confirmed in future. Please allow space for Addresses, Phone, Cell, Email and Web address.
Hi Quill42,
You are the winner of the stationary project for Tovin Industries.
We have had some commercial issues with the company name Tovin, and as this is a start up company, we have changed the name.
The new Company name is ZENTH Industries. I have the new logo file, how do I send this to you?
As such I have a new set of address and company name for you to change for the final design.
And the only contact details we want on all the stationary options that you supplied are as follows:
Web: www.zenth.example.nz
Email address: sales@zenth.example.nz
Phone: +6429184306
Contact: Owen Petrie General Manager
Please advise, if you require a different file type, I have .ai, .eps, .gif, .pdf, .png, .psd, .jpg, .tif
I look forward to hearing from you.
Best regards,
Owen

```html
<!DOCTYPE html>
<html lang="en">
<head>
<meta charset="utf-8">
<title>Tovin Industries – Business Card</title>
<link rel="stylesheet" href="https://fonts.googleapis.com/css2?family=Michroma&display=swap">
<style>
  :root {
    --page-bg: #e9eaec;
    --card-bg: #ffffff;
    --card-edge: #f1f3f5;
    --brand: #2f4b60;
    --text: #4a4f55;
    --muted: #7c838a;
    --icon: #8a9299;
    --rule: #c9d0d6;
  }
  * { margin: 0; padding: 0; box-sizing: border-box; }
  html, body {
    width: 1200px; height: 900px; overflow: hidden;
    background: var(--page-bg);
    font-family: "Michroma", sans-serif;
  }
  .canvas {
    position: relative; width: 1200px; height: 900px;
  }
  .card {
    position: absolute; left: 150px; top: 193px;
    width: 900px; height: 514px;
    background: linear-gradient(160deg, var(--card-bg) 0%, var(--card-bg) 60%, var(--card-edge) 100%);
    box-shadow: 0 10px 30px rgba(0,0,0,0.12);
  }
  .brand {
    position: absolute; left: 56px; top: 52px;
    display: flex; align-items: center; gap: 22px;
  }
  .brand-mark {
    width: 58px; height: 58px; background: var(--brand);
  }
  .brand-name {
    color: var(--brand); font-size: 30px; letter-spacing: 3px;
    text-transform: uppercase;
  }
  .contact-list {
    position: absolute; left: 56px; top: 290px;
    list-style: none; color: var(--text);
    font-size: 12.5px; line-height: 20px; letter-spacing: 0.6px;
    text-transform: uppercase;
  }
  .contact-item {
    display: flex; align-items: flex-start; gap: 12px;
  }
  .contact-item.address { margin-bottom: 18px; }
  .contact-icon { flex: none; width: 16px; height: 16px; margin-top: 2px; }
  .contact-icon circle { fill: var(--icon); }
  .contact-icon path { fill: none; stroke: #fff; stroke-width: 1.4; stroke-linecap: round; stroke-linejoin: round; }
  .contact-item .lowercase { text-transform: none; }
  .person {
    position: absolute; right: 56px; top: 340px; text-align: right;
    color: var(--brand); text-transform: uppercase; letter-spacing: 1.5px;
  }
  .person-name {
    font-size: 18px; padding-bottom: 8px;
    border-bottom: 1px solid var(--rule);
  }
  .person-title { font-size: 16px; margin-top: 8px; }
</style>
</head>
<body>
<main class="canvas">
  <section class="card">
    <header class="brand">
      <div class="brand-mark"></div>
      <div class="brand-name">Tovin Industries</div>
    </header>

    <ul class="contact-list">
      <li class="contact-item address">
        <svg class="contact-icon" viewBox="0 0 16 16"><circle cx="8" cy="8" r="8"/><path d="M8 12.5 C6 10 5 8.5 5 7 A3 3 0 0 1 11 7 C11 8.5 10 10 8 12.5 Z"/></svg>
        <span>PO Box 58491, Brackley, Christchurch<br>8245, New Zealand</span>
      </li>
      <li class="contact-item address">
        <svg class="contact-icon" viewBox="0 0 16 16"><circle cx="8" cy="8" r="8"/><path d="M8 12.5 C6 10 5 8.5 5 7 A3 3 0 0 1 11 7 C11 8.5 10 10 8 12.5 Z"/></svg>
        <span>14 Garnet Street, Fenwick,<br>Christchurch 8024, New Zealand</span>
      </li>
      <li class="contact-item">
        <svg class="contact-icon" viewBox="0 0 16 16"><circle cx="8" cy="8" r="8"/><path d="M5.5 4.5 L7 4.5 L7.6 6.6 L6.6 7.4 C7.1 8.5 7.7 9.1 8.7 9.5 L9.5 8.5 L11.5 9.1 L11.5 10.6 C8 11 5 8 5.5 4.5 Z"/></svg>
        <span>+64 3 555 0142</span>
      </li>
      <li class="contact-item">
        <svg class="contact-icon" viewBox="0 0 16 16"><circle cx="8" cy="8" r="8"/><path d="M6 4 H10 V12 H6 Z M7.5 10.5 H8.5"/></svg>
        <span>+64 29 184 306</span>
      </li>
      <li class="contact-item">
        <svg class="contact-icon" viewBox="0 0 16 16"><circle cx="8" cy="8" r="8"/><path d="M4.5 5.5 H11.5 V10.5 H4.5 Z M4.5 5.5 L8 8.3 L11.5 5.5"/></svg>
        <span class="lowercase">sales@tovin-works.example.nz</span>
      </li>
      <li class="contact-item">
        <svg class="contact-icon" viewBox="0 0 16 16"><circle cx="8" cy="8" r="8"/><path d="M8 4.2 A3.8 3.8 0 1 0 8 11.8 A3.8 3.8 0 1 0 8 4.2 M4.2 8 H11.8 M8 4.2 C6.5 6 6.5 10 8 11.8 M8 4.2 C9.5 6 9.5 10 8 11.8"/></svg>
        <span class="lowercase">www.tovin-works.example.nz</span>
      </li>
    </ul>

    <div class="person">
      <div class="person-name">Owen Petrie</div>
      <div class="person-title">General Manager</div>
    </div>
  </section>
</main>
</body>
</html>
```